Laser Hair Remova for all skin types

I want a post card to mail in an envelope. So both sides of the postcard can have information on it. I won't be addressing the postcard itself. I want it to target darker skinned women who are East Indian nationality. The type of laser we have can treat all skin types safely and effectively.
Updates

Project Deadline Extended
Reason: Due to the Holiday I would like to extend the deadline. Thanks!

Target Market(s)

women ages 18-40 moderate to higher income

the pictures attached are just examples although I like them and especially the body parts chart.

Industry/Entity Type

Hair

Colors
00a88f
00a98f

Requirements
Must have
• Can say somewhere on the postcard...
Imagine having Nothing to Hide...

Laser Hair Removal for ALL skin types

Make your appointment today

our website www.qvelmiskin.com
q.velmiskin@tornivo.com
612-408-2253
417 West Alder Rd
Plymouth, Mi. 48170

our specials:

lip or chin $30 per visit
lip and chin $50 per vist
underarms $40 per visit
bikini line $40 per visit

affordable packages available

consultations and test spots are always complimentary

```html
<!DOCTYPE html>
<html lang="en">
<head>
<meta charset="utf-8">
<title>Velmi Skin — Laser Hair Removal Postcard</title>
<link href="https://fonts.googleapis.com/css2?family=Great+Vibes&family=Montserrat:wght@300;400;600;700&display=swap" rel="stylesheet">
<style>
  :root {
    --backdrop: #e9e6e3;
    --card: #ffffff;
    --teal: #00dcd8;
    --ink: #111111;
    --taupe: #6f625e;
    --muted: #4a4a4a;
    --rule: #9a9a9a;
    --tile-bg: #000000;
    --photo-light: #f2f2f2;
    --photo-mid: #b9b9b9;
    --photo-dark: #6e6e6e;
  }
  * { box-sizing: border-box; margin: 0; padding: 0; }
  html, body {
    width: 1200px; height: 600px; overflow: hidden;
    background: var(--backdrop);
    font-family: "Montserrat", sans-serif;
  }
  .postcard {
    position: absolute; left: 95px; top: 105px;
    width: 1010px; height: 390px;
    background: var(--card);
    overflow: hidden;
  }
  .photo { position: absolute; }
  .photo--model-arm {
    left: 0; top: 0; width: 204px; height: 390px;
    background: linear-gradient(90deg, var(--photo-mid) 0%, var(--photo-light) 45%, var(--photo-mid) 100%);
  }
  .photo--model-seated {
    left: 505px; top: 0; width: 288px; height: 385px;
    background: radial-gradient(ellipse at 55% 50%, var(--photo-dark) 0%, var(--photo-mid) 45%, var(--photo-light) 80%);
  }
  .brand-tile {
    position: absolute; width: 120px; height: 120px;
    background: var(--tile-bg);
    display: flex; align-items: center; justify-content: center;
  }
  .brand-tile--front { left: 204px; top: 0; }
  .brand-tile--back { left: 878px; top: 17px; }
  .brand-name {
    color: var(--teal); font-family: "Montserrat", sans-serif;
    font-weight: 600; font-size: 13px; letter-spacing: 1px;
    text-transform: uppercase;
  }
  .headline {
    position: absolute; left: 205px; top: 124px;
    font-family: "Great Vibes", cursive; font-weight: 400;
    color: var(--teal); line-height: 1;
  }
  .headline__small { display: block; font-size: 22px; }
  .headline__large { display: block; font-size: 36px; margin-left: 10px; margin-top: -4px; }
  .pitch {
    position: absolute; left: 203px; top: 193px;
    color: var(--taupe); font-weight: 600; font-size: 11.5px; line-height: 17px;
    text-transform: uppercase;
  }
  .specials-title {
    position: absolute; left: 205px; top: 228px;
    font-family: "Great Vibes", cursive; font-weight: 400;
    color: var(--teal); font-size: 17px;
  }
  .specials {
    position: absolute; left: 205px; top: 251px;
    border-collapse: collapse; font-size: 11px; text-transform: uppercase; color: var(--muted);
  }
  .specials td { padding: 0; height: 15.5px; font-weight: 400; white-space: nowrap; }
  .specials .area { width: 83px; }
  .specials .price { color: var(--ink); font-weight: 700; font-size: 12px; padding-right: 5px; }
  .notes {
    position: absolute; left: 206px; top: 319px;
    color: var(--taupe); font-weight: 700; font-size: 8.2px; line-height: 13px; text-transform: uppercase;
    white-space: nowrap;
  }
  .contact-band {
    position: absolute; left: 205px; top: 346px; width: 298px; height: 43px;
    background: var(--teal); color: var(--ink);
    padding: 5px 0 0 8px; font-size: 12px; line-height: 17px;
  }
  .contact-band__line { display: flex; align-items: center; gap: 4px; white-space: nowrap; }
  .contact-band__phone { font-weight: 700; margin-right: 6px; }
  .contact-band svg { width: 9px; height: 9px; }
  .overlay-quote {
    position: absolute; left: 575px; top: 118px;
    font-family: "Great Vibes", cursive; font-weight: 400; color: #ffffff;
    font-size: 26px; line-height: 24px;
  }
  .overlay-quote span { display: block; }
  .overlay-quote span:nth-child(2) { margin-left: 18px; }
  .overlay-quote span:nth-child(3) { margin-left: 10px; }
  .overlay-quote span:nth-child(4) { margin-left: 2px; }
  .divider {
    position: absolute; left: 757px; top: 25px; height: 340px;
    border-left: 1px dotted var(--rule);
  }
  .address-lines { position: absolute; left: 767px; top: 200px; width: 231px; }
  .address-lines span {
    display: block; height: 32px; border-top: 1px dotted var(--rule);
  }
</style>
</head>
<body>
  <article class="postcard">
    <div class="photo photo--model-arm" role="img" aria-label="Black and white photo of a smiling woman in a white top raising one arm to show a smooth underarm"></div>

    <div class="brand-tile brand-tile--front"><span class="brand-name">Velmi Skin</span></div>

    <h1 class="headline">
      <span class="headline__small">imagine having</span>
      <span class="headline__large">nothing to hide..</span>
    </h1>

    <p class="pitch">Laser hair removal for all skin types<br>Make your appointment today</p>

    <h2 class="specials-title">our specials...</h2>
    <table class="specials">
      <tr><td class="area">Lip or chin</td><td><span class="price">$30</span>per visit</td></tr>
      <tr><td class="area">Lip and chin</td><td><span class="price">$50</span>per visit</td></tr>
      <tr><td class="area">Underarms</td><td><span class="price">$40</span>per visit</td></tr>
      <tr><td class="area">Bikini line</td><td><span class="price">$40</span>per visit</td></tr>
    </table>

    <p class="notes">Affordable packages available<br>Consultations and test spots are always complimentary</p>

    <div class="contact-band">
      <div class="contact-band__line">417 West Alder Rd. Harlow Falls MI 49302</div>
      <div class="contact-band__line">
        <svg viewBox="0 0 10 10" aria-hidden="true"><rect width="10" height="10" rx="1.5" fill="#111"/><path d="M3 2.2c.3 0 .6.9.6 1.1 0 .3-.5.4-.4.7.3.8.9 1.4 1.7 1.7.3.1.4-.4.7-.4.2 0 1.1.3 1.1.6 0 .7-.6 1.2-1.2 1.1C4 6.7 3.3 6 2.9 4.4 2.8 3.4 2.5 2.3 3 2.2z" fill="#00dcd8"/></svg>
        <span class="contact-band__phone">612-408-2253</span>
        <svg viewBox="0 0 10 10" aria-hidden="true"><rect width="10" height="10" rx="1.5" fill="#111"/><circle cx="5" cy="5" r="2.6" fill="none" stroke="#00dcd8" stroke-width="1"/></svg>
        <span>qvelmiskin.com</span>
      </div>
    </div>

    <div class="photo photo--model-seated" role="img" aria-label="Black and white photo of a seated woman with a flower in her hair, wrapped in a white towel, hugging her knees"></div>
    <p class="overlay-quote"><span>imagine</span><span>having</span><span>nothing</span><span>to hide..</span></p>

    <div class="divider"></div>
    <div class="brand-tile brand-tile--back"><span class="brand-name">Velmi Skin</span></div>
    <div class="address-lines"><span></span><span></span><span></span><span></span><span></span></div>
  </article>
</body>
</html>
```